Create modern and sleek business card for luxury real estate company

We're a "boutique" real estate office looking for a design that gets across a highly modern luxury brand. Blacks and whites are probably the best colors unless we try a silver foil for the logo. I've attached a version of our current logo here. I'd like to swap out the current font on there with Gotham Light Regular.

I'm looking to have one side of the card have the logo with the space for our agents info on the other side.

Target Market(s)

Young professionals in a "luxury" headspace

Industry/Entity Type

Real estate

Contact Information for Business Card

A place for agent name, cell number, website. The slogan "Simply Rethinking Real Estate".

Font styles to use
Other font styles liked:
• Gotham Regular

Colors

Designer to choose only greyscale colors for use in the design.

Requirements
Must have
• Matte black as the background color. Clean lines and use of contrast. A specific design aspect that will use silver foil.
Nice to have
• Up in the air on integrating a QR code
Should not have
• Any houses or other real estate related design (ex: a clip art house)

```html
<!DOCTYPE html>
<html lang="en">
<head>
<meta charset="UTF-8">
<title>Solace Realty – Business Card</title>
<link rel="stylesheet" href="https://fonts.googleapis.com/css2?family=Arimo:wght@400&display=swap">
<style>
  :root {
    --card-black: #151515;
    --silver: #cfcfcf;
    --silver-light: #f2f2f2;
    --silver-dark: #8e8e8e;
    --ink-white: #f4f4f4;
  }
  * { margin: 0; padding: 0; box-sizing: border-box; }
  html, body {
    width: 1200px;
    height: 617px;
    overflow: hidden;
    background: #ffffff;
  }
  .card {
    position: relative;
    width: 1200px;
    height: 617px;
    background: var(--card-black);
    font-family: "Arimo", Arial, sans-serif;
    color: var(--ink-white);
  }
  .brand-mark {
    position: absolute;
    left: 71px;
    top: 40px;
    width: 148px;
    height: 148px;
  }
  .brand-name {
    position: absolute;
    left: 250px;
    top: 58px;
    font-size: 58px;
    line-height: 64px;
    font-weight: 400;
    letter-spacing: 2px;
    color: var(--silver);
  }
  .agent-info {
    position: absolute;
    left: 88px;
    top: 392px;
    font-size: 31px;
    line-height: 44px;
    letter-spacing: 0.5px;
    color: var(--ink-white);
  }
  .foil-rule {
    position: absolute;
    left: 68px;
    top: 554px;
    width: 754px;
    height: 11px;
    background: linear-gradient(90deg, var(--silver-dark), var(--silver-light) 45%, var(--silver) 70%, var(--silver-dark));
  }
  .qr-slot {
    position: absolute;
    left: 921px;
    top: 335px;
    width: 208px;
    height: 208px;
    border: 3px dashed var(--ink-white);
  }
</style>
</head>
<body>
  <main class="card">
    <svg class="brand-mark" viewBox="0 0 148 148" aria-hidden="true">
      <circle cx="74" cy="74" r="70" fill="none" stroke="var(--silver)" stroke-width="4"/>
    </svg>
    <div class="brand-name">SOLACE<br>REALTY</div>

    <div class="agent-info">
      <p class="agent-name">YOUR NAME</p>
      <p class="agent-phone">+00 0000 0000</p>
      <p class="agent-web">WWW.YOURWEBSITE.COM</p>
    </div>

    <div class="foil-rule"></div>
    <div class="qr-slot" role="img" aria-label="Space reserved for QR code"></div>
  </main>
</body>
</html>
```